make a fireworks website

we are manufacturer of fireworks in Asia.
we need a HD fireworks website for showing product to all world customers.
we also need an register for member system,location, forum,products..etc
I added my Logo for the company.
brightpeonyhall.com.hk

and please message me if you have
any question.
here some example of website:
http://www.lanternmoth.com/
http://www.korvelmist.com/
http://www.tindle-orbwick.co.uk/
http://www.pemberlyspark.co.uk/

```html
<!DOCTYPE html>
<html lang="en">
<head>
<meta charset="utf-8">
<title>Bright Peony</title>
<link rel="stylesheet" href="https://fonts.googleapis.com/css2?family=Arimo:wght@400;700&display=swap">
<style>
:root{
  --bg:#1c1c1c;
  --bg-dark:#131313;
  --line:#3d3d3d;
  --heading:#e2e2e2;
  --text:#7a7a7a;
  --text-dim:#555;
  --title:#a3a3a3;
  --accent:#8e1d1d;
  --white:#fff;
  --footer:#121212;
}
*{margin:0;padding:0;box-sizing:border-box}
html,body{width:1200px;height:911px;overflow:hidden;background:var(--bg)}
body{font-family:"Arimo",Arial,sans-serif}
.page{position:relative;width:1366px;height:1037px;transform:scale(0.8785);transform-origin:0 0;
  background:repeating-linear-gradient(0deg,#1d1d1d 0 2px,#1a1a1a 2px 4px)}
.abs{position:absolute}
.logo-box{left:203px;top:0;width:232px;height:97px;background:#1f1f1f}
.logo{left:240px;top:42px;display:flex;align-items:center;gap:10px;color:var(--white);font-size:19px;font-weight:400;letter-spacing:.5px}
.logo-mark{width:14px;height:14px;border-radius:50%;background:#d6336c}
.header-rule{left:203px;top:97px;width:960px;height:1px;background:var(--line)}
.nav{top:51px;left:471px;display:flex;gap:20px;font-size:11px;color:#c8c8c8;letter-spacing:.2px}
.nav .active{color:var(--white)}
.search{left:963px;top:41px;width:191px;height:27px;background:var(--white);font-size:11px;color:#999;padding:8px 5px}
.search svg{position:absolute;right:8px;top:4px}
.hero{left:203px;top:118px;width:960px;height:327px;
  background:radial-gradient(ellipse at 25% 35%,#f08a7a 0,#c9456a 25%,transparent 55%),
  radial-gradient(ellipse at 80% 40%,#f29a86 0,#c5406a 28%,transparent 58%),
  radial-gradient(circle at 50% 60%,#5a2a8a 0,#2a1040 40%,#0a0510 75%)}
.news-bar{left:203px;top:455px;width:960px;height:31px;background:var(--bg-dark);font-size:11px;color:#666;padding:10px 20px}
.news-bar b{color:#888}
.dots{left:1047px;top:467px;display:flex;gap:8px}
.dots span{width:17px;height:7px;background:#3a3a3a}
.dots .on{background:var(--accent)}
.h2{top:507px;font-size:18px;font-weight:400;color:var(--heading)}
.post{left:218px;width:235px;font-size:12px;line-height:21px;color:var(--text)}
.post .meta{font-size:11px;line-height:14px;color:#777}
.post .meta a,.more{color:var(--accent);text-decoration:none}
.post .title{font-weight:700;color:var(--title);line-height:20px;margin-top:2px}
.more{font-size:12px}
.thumb{top:569px;width:312px;height:101px}
.thumb-products{left:483px;background:radial-gradient(ellipse at 50% 60%,#e3a040 0,#c24a3a 30%,#3a1a20 60%,#000 85%)}
.thumb-projects{left:815px;background:radial-gradient(ellipse at 40% 40%,#f29080 0,#b8406a 35%,#3a1838 70%,#0a050a 95%)}
.blurb{top:684px;width:300px;font-size:12px;line-height:21px;color:var(--text)}
.footer{left:0;top:801px;width:1366px;height:182px;background:var(--footer);border-top:1px solid #222}
.fcol{top:822px;width:230px}
.fcol h3{font-size:14px;color:#bbb;font-weight:700;margin-bottom:12px}
.fcol ul{list-style:none;font-size:10.5px;line-height:20px;color:var(--text-dim)}
.fcol li::before{content:"» ";color:var(--accent)}
.stack{font-size:10.5px;line-height:19px;color:var(--text-dim);margin-top:16px;letter-spacing:.3px}
.stack b{color:#666}
.social{display:flex;gap:12px;margin-top:10px}
.social span{width:16px;height:16px;border-radius:2px}
.bottom{left:0;top:983px;width:1366px;height:54px;background:#151515;border-top:1px solid #222}
.copy{left:213px;top:1004px;font-size:10.5px;color:#444;line-height:14px}
.copy nav{padding-left:5px;color:#555;font-weight:700}
.copy nav span{color:#2a4a6a;margin:0 6px}
.brand-foot{right:218px;top:1004px;font-size:11px;color:#555;font-weight:700}
</style>
</head>
<body>
<div class="page">
  <div class="abs logo-box"></div>
  <div class="abs logo"><span class="logo-mark"></span>Bright Peony</div>
  <nav class="abs nav"><span class="active">HOME</span><span>PRODUCTS</span><span>PROJECTS</span><span>ABOUT US</span><span>CONTACT US</span></nav>
  <div class="abs search">Search...
    <svg width="20" height="20" viewBox="0 0 20 20"><circle cx="8" cy="8" r="5.5" fill="none" stroke="#888" stroke-width="2"/><line x1="12" y1="12" x2="18" y2="18" stroke="#666" stroke-width="3"/></svg>
  </div>
  <div class="abs header-rule"></div>

  <div class="abs hero" role="img" aria-label="Fireworks bursting over an illuminated observation wheel at night"></div>
  <div class="abs news-bar"><b>Latest News:</b> Dipisicing elit, sed do eiusmod tempor incididunt ut labore et?</div>
  <div class="abs dots"><span></span><span></span><span class="on"></span><span></span></div>

  <h2 class="abs h2" style="left:218px">Our News</h2>
  <h2 class="abs h2" style="left:488px">Our Productst</h2>
  <h2 class="abs h2" style="left:820px">Our Projects</h2>

  <div class="abs post" style="top:563px">
    <div class="meta">12 Dec 2015 | <a href="#">0 comments</a></div>
    <div class="title">Duis nec porttitor lorem</div>
    <p>Mauris et nisi urna nonfaucibus magna. Integer lacus ante then ullamcorper ut vulputate..</p>
  </div>
  <div class="abs post" style="top:694px">
    <div class="meta">18 Dec 2015 | <a href="#">5 comments</a></div>
    <div class="title">Aenean interdum</div>
    <p>Vestibulum ante ipsum primis in faucibus orci luctus ultrices ante posuere.</p>
  </div>
  <a class="abs more" style="left:218px;top:780px" href="#">More News»</a>

  <div class="abs thumb thumb-products" role="img" aria-label="Colourful firework display product showcase"></div>
  <div class="abs thumb thumb-projects" role="img" aria-label="Firework show over an observation wheel project"></div>

  <div class="abs blurb" style="left:488px">
    <p>Lorem Ipsum is simply dummy text of the printing and typesetting industry. It has survived not only five centuries, but also the leap into electronic typesetting, remaining essentially unchanged.</p>
    <a class="more" href="#" style="display:block;margin-top:6px">Read More »</a>
  </div>
  <div class="abs blurb" style="left:820px">
    <p>Lorem Ipsum is simply dummy text of the printing and typesetting industry. It has survived not only five centuries, but also the leap into electronic typesetting, remaining essentially unchanged.</p>
    <a class="more" href="#" style="display:block;margin-top:6px">Read More »</a>
  </div>

  <footer class="abs footer"></footer>
  <div class="abs fcol" style="left:218px">
    <h3>About</h3>
    <ul><li>Lorem ipsum dolor sit amet</li><li>Nunc interdum dictum bibendum</li><li>Aliquam scelerisque</li><li>Pellentesque id est velit</li><li>Maecenas accumsan</li><li>Maecenas a odio id arcu</li></ul>
  </div>
  <div class="abs fcol" style="left:458px">
    <h3>Tweets</h3>
    <div class="stack">Lorem ipsum dolor sit amet<br><b>August 18th, 2015</b><br>Lorem ipsum dolor sit amet<br><b>August 19th, 2015</b><br>Lorem ipsum dolor sit amet<br><b>August 22th, 2015</b></div>
  </div>
  <div class="abs fcol" style="left:698px">
    <h3>Our Services</h3>
    <div class="stack"><b>Garden Fireworks</b><br>Remote fireworks<br><b>Rockets</b><br>Sparklers<br><b>Wedding fireworks</b><br>Chinese Lanterns</div>
  </div>
  <div class="abs fcol" style="left:938px">
    <h3>Contact</h3>
    <div class="stack"><b>+1 555.014.2290</b><br><b>contact@brightpeonyhall.com.hk</b><br>48 Lantern Row<br>Harbourview, KL 40210</div>
    <div class="social"><span style="background:#4aa8d8"></span><span style="background:#3b6cc4"></span><span style="background:#e8792a"></span></div>
  </div>

  <div class="abs bottom"></div>
  <div class="abs copy">© Copyright Bright Peony. All Rights Reserved
    <nav>Home<span>|</span>Contact<span>|</span>RSS</nav>
  </div>
  <div class="abs brand-foot">Bright Peony</div>
</div>
</body>
</html>
```